Kelvo Fitness Personal Training Business

I need a business card design with a logo for my personal training company. I'd like the colors to be a vibrant green and black. I'd like the logo to incorporate an anvil (or something similar). I train hardcore competitive athletes as well as soccer moms trying to get and/or stay in shape. I need a logo that will not pigeon hole me in one category or the other, but at the same time not be too intimidating to soccer moms, but will not be off putting to the more hardcore trainees. The design should be attention grabbing and aesthetic.
Target Market(s)
Hardcore athletes as well as average people just trying to get/stay in shape.
Industry/Entity Type
Training
Look and feel

```html
<!DOCTYPE html>
<html lang="en">
<head>
<meta charset="utf-8">
<title>Kelvo Fitness – Business Card</title>
<link rel="stylesheet" href="https://fonts.googleapis.com/css2?family=Source+Sans+3:wght@400;600;700&display=swap">
<style>
  :root {
    --backdrop: #4a403c;
    --card: #1d1d1d;
    --card-edge: #262626;
    --green: #6cbf3a;
    --text-light: #e6e6e6;
    --text-muted: #8a8a8a;
    --divider: #3a3a3a;
  }
  * { box-sizing: border-box; margin: 0; padding: 0; }
  html, body {
    width: 1200px; height: 776px; overflow: hidden;
    background: var(--backdrop);
    font-family: "Source Sans 3", sans-serif;
  }
  .canvas {
    width: 1200px; height: 776px;
    display: flex; align-items: center; justify-content: center; gap: 48px;
  }
  .card {
    width: 540px; height: 309px;
    background: linear-gradient(160deg, var(--card-edge), var(--card));
    box-shadow: 0 10px 24px rgba(0,0,0,.35);
    position: relative;
  }
  .wordmark { display: flex; flex-direction: column; }
  .wordmark-row { display: flex; align-items: center; gap: 12px; }
  .wordmark-square { width: 22px; height: 22px; background: var(--green); }
  .wordmark-name {
    font-weight: 700; color: var(--green); letter-spacing: .5px; line-height: 1;
  }
  .wordmark-tagline { color: var(--text-muted); font-weight: 400; margin-top: 4px; }

  .card-front { display: flex; align-items: center; justify-content: center; }
  .card-front .wordmark-name { font-size: 44px; }
  .card-front .wordmark-tagline { font-size: 18px; padding-left: 34px; }

  .card-back { display: flex; align-items: center; padding: 0 30px; }
  .card-back .wordmark { width: 230px; }
  .card-back .wordmark-square { width: 16px; height: 16px; gap: 8px; }
  .card-back .wordmark-name { font-size: 30px; }
  .card-back .wordmark-tagline { font-size: 13px; padding-left: 28px; }
  .divider { width: 1px; height: 150px; background: var(--divider); margin: 0 22px; }
  .contact { color: var(--text-light); font-size: 15px; line-height: 1.35; }
  .contact-name { color: var(--green); font-size: 25px; font-weight: 600; line-height: 1.1; }
  .contact-role { color: var(--text-light); font-size: 14px; margin-bottom: 8px; }
  .contact-address { margin-bottom: 6px; }
  .contact-list { list-style: none; }
  .contact-list li { display: flex; align-items: center; gap: 7px; }
  .contact-icon { width: 12px; height: 12px; fill: var(--green); flex: none; }
</style>
</head>
<body>
<main class="canvas">
  <section class="card card-front">
    <div class="wordmark">
      <div class="wordmark-row">
        <span class="wordmark-square"></span>
        <span class="wordmark-name">Kelvo Fitness</span>
      </div>
      <span class="wordmark-tagline">Personal Training Company</span>
    </div>
  </section>

  <section class="card card-back">
    <div class="wordmark">
      <div class="wordmark-row">
        <span class="wordmark-square"></span>
        <span class="wordmark-name">Kelvo Fitness</span>
      </div>
      <span class="wordmark-tagline">Personal Training Company</span>
    </div>
    <div class="divider"></div>
    <div class="contact">
      <p class="contact-name">Darren Holt</p>
      <p class="contact-role">Managing Member</p>
      <p class="contact-address">2210 Meridian Lane,<br>Fairbrook, CA 95014</p>
      <ul class="contact-list">
        <li><svg class="contact-icon" viewBox="0 0 12 12"><path d="M2.5 0.5l2 2.5-1.2 1.3c.7 1.6 2 2.9 3.6 3.6L8.2 6.7l2.5 2-1 2.3C5 11 1 7 1 1.5z"/></svg>(555) 204-7718</li>
        <li><svg class="contact-icon" viewBox="0 0 12 12"><rect x="3" y="0.5" width="6" height="4"/><rect x="0.5" y="4" width="11" height="6" rx="1"/><rect x="3" y="8" width="6" height="3.5"/></svg>(555) 204-7719</li>
        <li><svg class="contact-icon" viewBox="0 0 12 12"><path d="M3 0h6a1 1 0 0 1 1 1v10a1 1 0 0 1-1 1H3a1 1 0 0 1-1-1V1a1 1 0 0 1 1-1zm0 1.5v8h6v-8z"/></svg>(555) 318-4402</li>
        <li><svg class="contact-icon" viewBox="0 0 12 12"><path d="M0 2h12v8H0zM1 3l5 3.5L11 3v-.2H1z"/></svg>darren@kelvofit.com</li>
        <li><svg class="contact-icon" viewBox="0 0 12 12"><circle cx="6" cy="6" r="5.5"/><path d="M0.5 6h11M6 .5c-3 3-3 8 0 11M6 .5c3 3 3 8 0 11" stroke="#1d1d1d" stroke-width=".8" fill="none"/></svg>www.kelvofit.com</li>
      </ul>
    </div>
  </section>
</main>
</body>
</html>
```